Corvane Tables business cards

I’d like a business card design that includes my logo, a tag line and my contact info. Black, textured background. My contact info color should match the orange and blue gradients. Tagline under logo: “Wooden Tables and Furniture of the Highest Quality”

Target Market(s)

High end furniture buyers

Contact Information for Business Card

Contact info, logo and tagline

```html
<!DOCTYPE html>
<html lang="en">
<head>
<meta charset="utf-8">
<title>Corvane Tables — Business Cards</title>
<link rel="stylesheet" href="https://fonts.googleapis.com/css2?family=Montserrat:wght@400;500;700&display=swap">
<style>
  :root {
    --stage: #1c1c1e;
    --card-black: #050505;
    --card-white: #ffffff;
    --brand-blue: #0a55b0;
    --brand-orange: #eb7424;
    --tagline-text: #ffffff;
  }
  * { box-sizing: border-box; margin: 0; padding: 0; }
  html, body {
    width: 1200px; height: 1015px; overflow: hidden;
    background: var(--stage);
    font-family: "Montserrat", sans-serif;
  }
  .canvas { position: relative; width: 1200px; height: 1015px; }

  .card {
    position: absolute; left: 230px; width: 740px; height: 420px;
    overflow: hidden;
    box-shadow: 0 14px 30px rgba(0,0,0,0.6);
  }

  /* Front */
  .card--front { top: 60px; background: var(--card-black); }
  .front-wordmark {
    position: absolute; left: 0; right: 0; top: 120px; height: 72px;
    display: flex; align-items: center; justify-content: center;
  }
  .brand-name {
    font-family: "Montserrat", sans-serif; font-weight: 500;
    color: var(--brand-blue); letter-spacing: 1px; white-space: nowrap; line-height: 1;
  }
  .front-wordmark .brand-name { font-size: 58px; }
  .brand-dot { border-radius: 50%; background: var(--brand-orange); flex: none; }
  .front-wordmark .brand-dot { width: 22px; height: 22px; margin-right: 16px; }
  .tagline-band {
    position: absolute; left: 0; right: 0; top: 300px; height: 56px;
    background: var(--brand-blue);
    display: flex; align-items: center; justify-content: center;
  }
  .tagline {
    color: var(--tagline-text); font-size: 21px; font-weight: 500; letter-spacing: 0.6px;
  }

  /* Back */
  .card--back { top: 535px; background: var(--card-white); }
  .back-wordmark {
    position: absolute; left: 40px; top: 178px; width: 340px; height: 44px;
    display: flex; align-items: center;
  }
  .back-wordmark .brand-dot { width: 14px; height: 14px; margin-right: 10px; }
  .back-wordmark .brand-name { font-size: 34px; }
  .divider {
    position: absolute; left: 392px; top: 70px; width: 1px; height: 230px;
    background: var(--brand-orange);
  }
  .contact { position: absolute; left: 420px; top: 72px; color: var(--brand-blue); }
  .contact-name { font-size: 30px; font-weight: 700; line-height: 1; }
  .contact-name .first { color: var(--brand-orange); }
  .contact-role { font-size: 17px; font-weight: 500; margin-top: 6px; }
  .contact-list { list-style: none; margin-top: 20px; }
  .contact-list li {
    display: flex; align-items: center; font-size: 17px; font-weight: 500;
    line-height: 1; margin-bottom: 10px;
  }
  .contact-list svg { width: 16px; height: 16px; margin-right: 8px; flex: none; }
  .contact-address { font-size: 17px; font-weight: 500; line-height: 1.3; margin-top: 12px; }

  .foot-bar--orange {
    position: absolute; left: 0; bottom: 0; width: 480px; height: 30px;
    background: var(--brand-orange);
  }
  .foot-bar--blue {
    position: absolute; left: 490px; right: 0; bottom: 0; height: 30px;
    background: var(--brand-blue);
  }
</style>
</head>
<body>
<main class="canvas">

  <section class="card card--front" aria-label="Card front">
    <div class="front-wordmark">
      <span class="brand-dot"></span><span class="brand-name">Corvane Tables</span>
    </div>
    <div class="tagline-band">
      <p class="tagline">Wooden Tables and Furniture of the Highest Quality</p>
    </div>
  </section>

  <section class="card card--back" aria-label="Card back">
    <div class="back-wordmark">
      <span class="brand-dot"></span><span class="brand-name">Corvane Tables</span>
    </div>
    <div class="divider"></div>
    <div class="contact">
      <p class="contact-name"><span class="first">Marcus</span> Hale</p>
      <p class="contact-role">Managing Director</p>
      <ul class="contact-list">
        <li>
          <svg viewBox="0 0 16 16" aria-hidden="true"><path d="M3.5 1.5l2.5 0.5 1 3-1.6 1.2a8 8 0 0 0 4.4 4.4L11 9l3 1 .5 2.5-1.8 1.8C7 14 2 9 1.7 3.3z" fill="var(--brand-orange)"/></svg>
          044-555 018 274
        </li>
        <li>
          <svg viewBox="0 0 16 16" aria-hidden="true"><rect x="1" y="3" width="14" height="10" fill="var(--brand-orange)"/><path d="M1 3l7 6 7-6" fill="none" stroke="#fff" stroke-width="1.3"/></svg>
          info@corvanemail.com
        </li>
        <li>
          <svg viewBox="0 0 16 16" aria-hidden="true"><g fill="none" stroke="var(--brand-orange)" stroke-width="1.4"><circle cx="8" cy="8" r="6.5"/><ellipse cx="8" cy="8" rx="2.8" ry="6.5"/><path d="M1.5 8h13M2.5 4.7h11M2.5 11.3h11"/></g></svg>
          www.corvanetables.com
        </li>
      </ul>
      <p class="contact-address">218 Harrow Lane, Suite 4<br>60419, Eastmere</p>
    </div>
    <div class="foot-bar--orange"></div>
    <div class="foot-bar--blue"></div>
  </section>

</main>
</body>
</html>
```